People Search Directory Needs a Web Design

We need a web design for a new web site called Kestrel Lineage Lookups. We provide free directory information, such as name, phone, address, and email. We also provide other non-white pages information such as the person's relatives, historical records to help identify the person, and link the data so people can find connections. For example, by clicking on an address that a person lives at, you can find other people who might currently (or previously) have lived at that address.

We have a very basic web page that contains a lot of public records data. The page can look very busy. We need it to be concise, where the white pages type of information is easily identifiable, but people also realize the usefulness of the surrounding data (such as possible relatives, email address, historical phone numbers, etc).

The web page also promotes an annual membership to get more in-depth information on people. These Kestrel Lineage Lookups include a criminal records check, property records, and other information.

Industry/Entity Type

Property

Requirements
Must have
• Attached is an example design we put together. We want the design to be snazzier, have more information architecture thought put into it, etc.

```html
<!DOCTYPE html>
<html lang="en">
<head>
<meta charset="utf-8">
<title>Kestrel Lineage Lookups — People Search</title>
<link href="https://fonts.googleapis.com/css2?family=Arimo:wght@400;700&display=swap" rel="stylesheet">
<style>
:root{
  --ink:#2f3338;
  --muted:#8b9096;
  --blue:#2a8fd0;
  --blue-dark:#1760a8;
  --green:#6fb92c;
  --orange:#f59a4f;
  --page:#eef0f3;
  --bar:#efeff0;
  --line:#d6d9dd;
  --white:#ffffff;
}
*{box-sizing:border-box;margin:0;padding:0}
html,body{width:1200px;height:1148px;overflow:hidden}
body{position:relative;background:var(--page);font-family:"Arimo",Arial,sans-serif;color:var(--ink)}
.abs{position:absolute}
.header{left:0;top:0;width:1200px;height:133px;background:linear-gradient(#f4f4f6,#eaeaee);border-bottom:1px solid #e0e0e4}
.brand{left:96px;top:56px;display:flex;align-items:center;gap:12px}
.brand-name{font-size:30px;font-weight:700;color:var(--blue-dark);letter-spacing:.5px;text-transform:uppercase}
.brand-mark{width:28px;height:28px;background:var(--green);border-radius:4px}
.nav{left:747px;top:68px;display:flex;gap:26px;align-items:center;font-size:15px;color:var(--muted)}
.nav .current{background:var(--blue-dark);color:#fff;font-weight:700;padding:4px 9px;border-radius:2px}
.btn-orange{background:var(--orange);color:#fff;font-size:15px;display:flex;align-items:center;justify-content:center;border-radius:3px;border:1px solid #e48436;white-space:nowrap;z-index:5}
.search-band{left:0;top:134px;width:1200px;height:96px;background:var(--white);border-bottom:1px solid var(--line)}
.field-label{font-size:15px;color:var(--ink);top:147px}
.field{top:171px;height:36px;background:#f2f3f5;border:1px solid #d3d6da;border-radius:3px;font-size:14px;color:#8d949a;padding:10px 12px}
.select-arrow{right:10px;top:14px;border:5px solid transparent;border-top-color:#9aa0a6}
.search-btn{left:963px;top:169px;width:108px;height:40px;background:linear-gradient(#2a7fd0,#1258a6);color:#fff;font-weight:700;font-size:19px;border-radius:4px;display:flex;align-items:center;justify-content:center}
.card{left:93px;top:261px;width:1003px;height:802px;background:#fff;border:1px solid #d8dbdf;border-radius:6px;overflow:hidden}
.sidebar{left:787px;top:261px;width:309px;height:802px;background:linear-gradient(90deg,#f1f2f4,#fff 30%);border-left:1px solid #e2e4e7}
.person-head{left:112px;top:276px;display:flex;align-items:center;gap:10px;white-space:nowrap}
.person-name{font-size:17px;color:var(--blue)}
.person-sep{font-size:13px;color:#b8bcc0}
.person-age{font-size:15px;color:var(--muted)}
.more-info{width:67px;height:25px;background:var(--blue-dark);color:#fff;font-size:12px;font-weight:700;display:flex;align-items:center;justify-content:center;border-radius:2px}
.view-link{right:438px;top:282px;font-size:12px;color:var(--ink);white-space:nowrap}
.row{left:109px;width:662px;height:40px;display:flex;align-items:center;font-size:14px;padding-left:52px;white-space:nowrap}
.row.shaded{background:var(--bar)}
.row svg{position:absolute;left:14px}
.row a{color:var(--blue);text-decoration:none;margin-left:5px}
.tabs{left:109px;top:564px;width:662px;height:46px;background:#f4f4f6;border-bottom:1px solid var(--line)}
.tab{top:564px;height:46px;font-size:14px;font-weight:700;display:flex;align-items:center;justify-content:center;white-space:nowrap}
.tab.active{background:#fff;border-top:2px solid var(--blue);height:47px}
.relatives{left:128px;top:632px;list-style:none;font-size:12px;line-height:20.5px}
.promo{left:120px;top:827px;width:641px;height:204px;background:#f6f7f8;border:1px solid #dfe1e4;border-radius:6px}
.promo-title{left:142px;top:841px;width:610px;font-size:18px;font-weight:700;color:#3b4047;white-space:nowrap}
.promo-title span{color:var(--blue)}
.doc{left:141px;top:873px;width:99px;height:113px;background:linear-gradient(#f3dfae,#e6c987);border-radius:4px}
.feature{font-size:14px;display:flex;align-items:center;gap:12px;white-space:nowrap}
.green-btn{left:131px;top:997px;width:620px;height:28px;background:linear-gradient(#8fcf3e,#5ea923);color:#fff;font-weight:700;font-size:13px;display:flex;align-items:center;justify-content:center;border-radius:3px}
.side-title{left:808px;top:277px;font-size:16px;font-weight:700;white-space:nowrap}
.side-text{left:807px;top:307px;width:280px;font-size:14px;line-height:17.5px}
.side-btn{left:807px;top:397px;width:270px;height:27px;background:linear-gradient(#2a7fd0,#1258a6);color:#fff;font-size:12px;font-weight:700;display:flex;align-items:center;justify-content:center;border-radius:2px}
.map{left:797px;width:291px;border-radius:4px}
.map.street{top:457px;height:275px;background:linear-gradient(135deg,#f1efe9,#e4e1d8)}
.map.aerial{top:755px;height:273px;background:linear-gradient(135deg,#6c7a5d,#8d8f86)}
.footer-nav{left:95px;top:1080px;display:flex;gap:26px;align-items:center;font-size:13px;color:#5a5f66}
.footer-nav .current{background:var(--green);color:#fff;padding:6px 8px;border-radius:2px}
.copyright{left:101px;top:1122px;font-size:12px;color:#5a5f66}
</style>
</head>
<body>
<header class="abs header"></header>
<div class="abs brand"><span class="brand-name">Kestrel Lineage Lookups</span><span class="brand-mark"></span></div>
<nav class="abs nav"><span class="current">Home</span><span>About</span><span>People Directory</span><span>Contact</span></nav>

<section class="abs search-band"></section>
<div class="abs btn-orange" style="left:921px;top:117px;width:181px;height:28px">Get Annual Membership</div>
<span class="abs field-label" style="left:104px">First Name</span>
<span class="abs field-label" style="left:316px">M.I.</span>
<span class="abs field-label" style="left:384px">Last Name</span>
<span class="abs field-label" style="left:595px">City</span>
<span class="abs field-label" style="left:775px">State</span>
<div class="abs field" style="left:101px;width:196px">rosalind</div>
<div class="abs field" style="left:313px;width:52px"></div>
<div class="abs field" style="left:381px;width:195px">whitfield</div>
<div class="abs field" style="left:593px;width:164px"></div>
<div class="abs field" style="left:773px;width:175px">All States<span class="abs select-arrow"></span></div>
<div class="abs search-btn">Search</div>

<main class="abs card"></main>
<aside class="abs sidebar"></aside>

<div class="abs person-head">
  <span class="person-name">Rosalind K Whitfield</span>
  <span class="person-sep">///</span>
  <span class="person-age">Age 45</span>
  <span class="more-info">More Info</span>
</div>
<span class="abs view-link">Viwe Rosalind's Background Report &gt;&gt;</span>

<div class="abs row shaded" style="top:313px">
  <svg width="24" height="24" viewBox="0 0 24 24"><path d="M5 3l4 1 1 5-2 2a12 12 0 0 0 5 5l2-2 5 1 1 4c-1 2-3 3-5 3C10 21 3 14 3 8c0-2 1-4 2-5z" fill="#3a3f45"/></svg>
  (555) 214-0937</div>
<div class="abs row" style="top:357px">
  <svg width="24" height="24" viewBox="0 0 24 24"><path d="M12 2L1 12h3v10h6v-6h4v6h6V12h3z" fill="#3a3f45"/></svg>
  42 Alder Ln Brookhaven, NY 14702</div>
<div class="abs row shaded" style="top:401px;line-height:16px;flex-direction:column;align-items:flex-start;justify-content:center">
  <svg width="24" height="24" viewBox="0 0 24 24" style="top:8px"><rect x="1" y="5" width="22" height="15" rx="1" fill="#3a3f45"/><path d="M2 6l10 8 10-8" stroke="#fff" stroke-width="2" fill="none"/></svg>
  <span>rk58wav@mailhaven.net</span><span>doubler@mailhaven.net</span></div>
<div class="abs row" style="top:445px">
  <svg width="34" height="24" viewBox="0 0 34 24"><circle cx="7" cy="8" r="5" stroke="#3a3f45" stroke-width="2.5" fill="none"/><circle cx="27" cy="16" r="5" stroke="#3a3f45" stroke-width="2.5" fill="none"/><path d="M12 10l10 4" stroke="#3a3f45" stroke-width="2.5"/></svg>
  Check Nationwide Criminal Recoreds For<a>Rosalind K Whitfield &gt;&gt;</a></div>
<div class="abs row shaded" style="top:488px">
  <svg width="24" height="24" viewBox="0 0 24 24"><circle cx="14" cy="9" r="6" stroke="#3a3f45" stroke-width="2.5" fill="none"/><path d="M9 14l-6 7" stroke="#3a3f45" stroke-width="3"/></svg>
  Advanced Background Report on<a>Rosalind K Whitfield &gt;&gt;</a></div>

<div class="abs tabs"></div>
<div class="abs tab active" style="left:140px;width:163px">Possible Relatives</div>
<div class="abs tab" style="left:320px;width:200px">Previous Phone Numbers</div>
<div class="abs tab" style="left:555px;width:180px">Previous Addresses</div>

<ul class="abs relatives">
  <li>Martin Ellis Whitfield</li><li>Gerald W Whitfieldsr</li><li>Carter J Whitfield</li>
  <li>Nora M Whitfield</li><li>Lorraine E Whitfield</li><li>Ivy D Whitfield</li>
  <li>Peter J Whitfield</li><li>Samuel Owen Whitfield</li><li>Marissa D Whitfield</li>
</ul>

<section class="abs promo"></section>
<h2 class="abs promo-title">Want more in-depth information on <span>Rosalind K Whitfield</span> ?</h2>
<div class="abs doc" role="img" aria-label="Illustration of a paper case file folder"></div>
<div class="abs feature" style="left:267px;top:890px"><svg width="28" height="22" viewBox="0 0 28 22"><path d="M2 12l8 8L26 2" stroke="#6fb92c" stroke-width="5" fill="none"/></svg>Name and AKAs</div>
<div class="abs feature" style="left:267px;top:922px"><svg width="28" height="22" viewBox="0 0 28 22"><path d="M2 12l8 8L26 2" stroke="#6fb92c" stroke-width="5" fill="none"/></svg>Up to 40-year address history</div>
<div class="abs feature" style="left:267px;top:954px"><svg width="28" height="22" viewBox="0 0 28 22"><path d="M2 12l8 8L26 2" stroke="#6fb92c" stroke-width="5" fill="none"/></svg>Date of birth</div>
<div class="abs feature" style="left:552px;top:890px"><svg width="28" height="22" viewBox="0 0 28 22"><path d="M2 12l8 8L26 2" stroke="#6fb92c" stroke-width="5" fill="none"/></svg>Evictions &amp; bankruptcies</div>
<div class="abs feature" style="left:552px;top:922px"><svg width="28" height="22" viewBox="0 0 28 22"><path d="M2 12l8 8L26 2" stroke="#6fb92c" stroke-width="5" fill="none"/></svg>Property records</div>
<div class="abs feature" style="left:552px;top:954px"><svg width="28" height="22" viewBox="0 0 28 22"><path d="M2 12l8 8L26 2" stroke="#6fb92c" stroke-width="5" fill="none"/></svg>Criminal records check</div>
<div class="abs green-btn">Get Advance Background Report</div>

<h3 class="abs side-title">What's in your backgroynd report ?</h3>
<p class="abs side-text">See what records are publicly available in your background report. Also, check out the public records in reports for your friends and family.</p>
<div class="abs side-btn">Check My Background Report</div>
<div class="abs map street" role="img" aria-label="Street map of the neighborhood around the listed address"></div>
<div class="abs map aerial" role="img" aria-label="Aerial view of the listed address"></div>

<nav class="abs footer-nav"><span class="current">Home</span><span>About</span><span>People Directory</span><span>FAQs</span><span>Privacy</span><span>Terms</span><span>Contact</span></nav>
<div class="abs btn-orange" style="left:915px;top:1083px;width:180px;height:26px">Get Annual Membership</div>
<p class="abs copyright">Copyright © 2012 KestrelLineageLookups.com</p>
</body>
</html>
```